Package Design for Toe Cozy Countdown Box™

Looking to have the 2018 edition of our annual Toe Cozy Countdown Box™ graphics designed. The packaging is a complex dye the we already have, so positioning and dimensions are not an option.

If you can make the design a 4-color (spot) design, we're open to that, otherwise full CMYK is perfectly acceptable.

Attached are the 2016 & 2017 for reference. You can use the 2017 file as the best option for starting as a template.

Industry/Entity Type

Fashion

Colors

Designer to choose colors to be used in the design.

Requirements
Must have
• The numbers 1 through 24 must stay in the same position, but font can change.
Nice to have
• Pattern/design will match on seem where box is attached.

```html
<!DOCTYPE html>
<html lang="en">
<head>
<meta charset="utf-8">
<title>Toe Cozy Countdown Box™ — 2018 Lid</title>
<link href="https://fonts.googleapis.com/css2?family=Nunito:wght@800&display=swap" rel="stylesheet">
<style>
  :root {
    --canvas: #f2f0ec;
    --lid-red: #b11e2b;
    --side-red: #6a1018;
    --snow: #ffffff;
    --gold: #b88a58;
    --door-line: rgba(255,255,255,0.18);
    --door-line-light: rgba(120,100,90,0.25);
  }
  html, body {
    margin: 0;
    width: 1200px;
    height: 1200px;
    overflow: hidden;
    background: var(--canvas);
  }
  .package {
    position: absolute;
    left: 170px;
    top: 80px;
    width: 860px;
    height: 1040px;
    display: flex;
    box-shadow: 0 10px 30px rgba(0,0,0,0.12);
  }
  .lid {
    position: relative;
    width: 760px;
    height: 1040px;
    background: var(--snow);
    overflow: hidden;
  }
  .night-sky {
    position: absolute;
    left: 0;
    top: 0;
    width: 760px;
    height: 646px;
    background: var(--lid-red);
  }
  .village-skyline {
    position: absolute;
    left: 0;
    top: 646px;
    width: 760px;
    height: 74px;
    background: linear-gradient(to bottom, var(--lid-red) 0%, #d98a91 45%, var(--snow) 100%);
  }
  .doors {
    position: absolute;
    left: 24px;
    right: 24px;
    display: grid;
    grid-template-columns: repeat(4, 1fr);
    grid-auto-rows: 140px;
    gap: 14px;
  }
  .doors-sky { top: 24px; }
  .doors-snow { top: 734px; }
  .door {
    display: flex;
    align-items: center;
    justify-content: center;
    border: 2px dashed var(--door-line);
    border-radius: 22px;
    font-family: "Nunito", sans-serif;
    font-weight: 800;
    font-size: 72px;
    line-height: 1;
    color: var(--gold);
    letter-spacing: 2px;
  }
  .doors-snow .door { border-color: var(--door-line-light); }
  .side-panel {
    position: relative;
    width: 100px;
    height: 1040px;
    background: var(--side-red);
  }
  .brand-name {
    position: absolute;
    left: 50%;
    top: 560px;
    transform: translateX(-50%) rotate(90deg);
    font-family: "Nunito", sans-serif;
    font-weight: 800;
    font-size: 30px;
    color: var(--snow);
    white-space: nowrap;
  }
  .reindeer-art {
    position: absolute;
    left: 15px;
    top: 700px;
    width: 70px;
    height: 160px;
    background: linear-gradient(to bottom, #8a2a33, #5a0d14);
    border-radius: 8px;
  }
</style>
</head>
<body>
  <main class="package">
    <section class="lid">
      <div class="night-sky"></div>
      <div class="village-skyline" role="img" aria-label="White silhouette of a snowy village with houses and fir trees"></div>
      <div class="doors doors-sky">
        <div class="door">1</div><div class="door">21</div><div class="door">12</div><div class="door">7</div>
        <div class="door">10</div><div class="door">23</div><div class="door">4</div><div class="door">16</div>
        <div class="door">5</div><div class="door">13</div><div class="door">17</div><div class="door">9</div>
        <div class="door">18</div><div class="door">20</div><div class="door">8</div><div class="door">2</div>
      </div>
      <div class="doors doors-snow">
        <div class="door">15</div><div class="door">6</div><div class="door">14</div><div class="door">22</div>
        <div class="door">19</div><div class="door">3</div><div class="door">11</div><div class="door">24</div>
      </div>
    </section>
    <aside class="side-panel">
      <div class="brand-name">Toe Cozy</div>
      <div class="reindeer-art" role="img" aria-label="Leaping reindeer illustration"></div>
    </aside>
  </main>
</body>
</html>
```